Insurance company needs a business card design

We need a business card design for a Massachusetts-based insurance company Veloria Insurance, LLC. We provide auto insurance to Hispanic (Spanish- or Portuguese-speaking) immigrants in the United States. We will give these business cards to auto dealers where such customers typically go to purchase vehicles. We will provide a solution to the dealers to provide easy insurance to the customers buying cars at their dealerships. Veloria is the Spanish word for protection.
Contact Information for Business Card
Name, Designation, Company Name, Address, Phone Number, Email, Website
Look and feel
Each slider illustrates characteristics of the customer's brand and the style your logo design should communicate.

```html
<!DOCTYPE html>
<html lang="en">
<head>
<meta charset="utf-8">
<title>Veloria Insurance – Business Card</title>
<link href="https://fonts.googleapis.com/css2?family=Montserrat:wght@400;500;700&display=swap" rel="stylesheet">
<style>
  :root {
    --bg: #b9b9b9;
    --card: #ffffff;
    --orange: #f08a12;
    --blue: #1d5a8e;
    --blue-dark: #0f467a;
    --ink: #2e2e2e;
    --silver: #d6d6d6;
    --faint: #ececec;
  }
  html, body {
    margin: 0;
    width: 1200px;
    height: 876px;
    overflow: hidden;
    background: var(--bg);
    font-family: "Montserrat", sans-serif;
  }
  .stage {
    position: relative;
    width: 1200px;
    height: 876px;
  }
  .card {
    position: absolute;
    width: 525px;
    height: 300px;
    background: var(--card);
    overflow: hidden;
    box-shadow: 0 10px 24px rgba(0,0,0,.25);
  }
  .card--front { left: 630px; top: 150px; }
  .card--back  { left: 45px;  top: 430px; }

  .band {
    position: absolute;
    left: 0; right: 0; bottom: 0;
    height: 46px;
    display: flex;
    align-items: center;
    justify-content: center;
    border-top: 4px solid var(--silver);
    color: #fff;
    font-size: 11px;
    letter-spacing: 4px;
  }
  .band--orange { background: var(--orange); }
  .band--blue { background: linear-gradient(90deg, var(--blue-dark), var(--blue)); }

  .decor {
    position: absolute;
    background: radial-gradient(ellipse at center, var(--faint) 0%, rgba(236,236,236,.5) 55%, rgba(255,255,255,0) 75%);
  }
  .card--front .decor { right: -20px; top: 40px; width: 300px; height: 220px; }
  .card--back .decor { left: -30px; top: -30px; width: 260px; height: 240px; }

  .brand {
    position: absolute;
    display: flex;
    align-items: center;
    gap: 10px;
  }
  .brand__mark {
    width: 14px; height: 14px;
    background: var(--orange);
  }
  .brand__name {
    color: var(--blue);
    font-weight: 700;
    letter-spacing: 1px;
    line-height: 1;
  }
  .card--front .brand { left: 130px; top: 95px; }
  .card--front .brand__name { font-size: 44px; }
  .card--back .brand { left: 250px; top: 40px; }
  .card--back .brand__name { font-size: 28px; }

  .person {
    position: absolute;
    left: 150px; top: 100px;
    margin: 0;
    font-size: 40px;
    font-weight: 500;
    letter-spacing: 1px;
    color: var(--blue);
    line-height: 1;
  }
  .person__last { color: var(--orange); font-weight: 700; }

  .contact {
    position: absolute;
    left: 150px; top: 160px;
    margin: 0; padding: 0;
    list-style: none;
    font-size: 12px;
    color: var(--ink);
    line-height: 1.45;
  }
  .contact li { display: flex; gap: 8px; align-items: flex-start; }
  .contact svg { width: 11px; height: 11px; margin-top: 3px; flex: none; fill: var(--orange); }
</style>
</head>
<body>
<main class="stage">

  <section class="card card--front">
    <div class="decor" role="img" aria-label="Faint line-art decoration"></div>
    <div class="brand">
      <span class="brand__mark"></span>
      <span class="brand__name">VELORIA INSURANCE</span>
    </div>
    <div class="band band--orange">www.veloriainsure.com</div>
  </section>

  <section class="card card--back">
    <div class="decor" role="img" aria-label="Faint line-art decoration"></div>
    <div class="brand">
      <span class="brand__mark"></span>
      <span class="brand__name">VELORIA INSURANCE</span>
    </div>
    <h1 class="person">LOREM <span class="person__last">IPSUM</span></h1>
    <ul class="contact">
      <li>
        <svg viewBox="0 0 12 12"><path d="M2 1h3l1 3-2 1a7 7 0 0 0 3 3l1-2 3 1v3c-6 0-9-3-9-9z"/></svg>
        555 0142 321
      </li>
      <li>
        <svg viewBox="0 0 12 12"><path d="M0 2h12v8H0z M0 2l6 4 6-4" /></svg>
        hello@veloriainsure.com
      </li>
      <li>
        <svg viewBox="0 0 12 12"><path d="M6 0a4 4 0 0 1 4 4c0 3-4 8-4 8S2 7 2 4a4 4 0 0 1 4-4zm0 2.5a1.5 1.5 0 1 0 0 3 1.5 1.5 0 0 0 0-3z"/></svg>
        <span>0/00 lorem ipsum, loremipsum<br>loremipsum-0000</span>
      </li>
    </ul>
    <div class="band band--blue">www.veloriainsure.com</div>
  </section>

</main>
</body>
</html>
```